Motion Nest Business Cards

Can all designers please apply the following info on their designs' back-side of the business card: (please see brief file upload ('Info for backside...' - for required info, colours & layout)

SPECIALISING IN INDIVIDUAL PILATES INSTRUCTION
MATWORK – including small apparatus
and STUDIO:
VIVANTE 3 GLIDER
LADDER BARREL
COUNTOUR BARREL
FLEXI DOME
VIM STOOL
KIM-O-LAN

Business Cards for Motion Nest - applying the Motion Nest logo design selected earlier.
Note the business card requires both a front and back side. Please refer to two uploaded ppt-files for type of info required to be displayed, and rough position of where info could be. Require innovative / fresh approach to business card design and use of colour by designers now. Please refer to and use logo as uploaded - also for potential business card colour application.

Dear Designers,

Please note the additional inclusion / upload of two draft ppt-files that try to show where I want what type of information, for both the front & back sides of the required business card, plus an attempt at showing the high-level concept / idea of business info position.

As my 'drafts' obviously lack colour and any ability towards innovative card design or approach – I now rely on your vastly superior graphic design abilities to produce a really great business card for my business…

Looking forward to your submissions!

Kind regards, Merika for: Motion Nest 

Hello all Designers,

Can all designers please apply the following info on their designs' back-side of the business card: (please see / refer to the Brief and specifically the file upload ('Info for backside...' - for required info, colours & layout) - for the backside of the business card).

Info content (without colour, layout etc.):

and STUDIO:

VIVANTE 3 GLIDER

LADDER BARREL

COUNTOUR BARREL

FLEXI DOME

VIM STOOL

KIM-O-LAN

Thank you to all designers that submitted for consideration!

With regards,

Motion Nest

```html
<!DOCTYPE html>
<html lang="en">
<head>
<meta charset="utf-8">
<title>Motion Nest Business Cards</title>
<link rel="stylesheet" href="https://fonts.googleapis.com/css2?family=Roboto+Slab:wght@300&family=Roboto+Condensed:wght@400;700&display=swap">
<style>
  :root {
    --bg: #e4e4e2;
    --card: #ffffff;
    --green: #466a2e;
    --orange: #e0532a;
    --ink: #1d1d1b;
  }
  * { box-sizing: border-box; margin: 0; padding: 0; }
  html, body { width: 1200px; height: 1000px; overflow: hidden; }
  body { background: var(--bg); font-family: "Roboto Condensed", Arial, sans-serif; position: relative; }

  .card {
    position: absolute;
    width: 560px;
    height: 340px;
    background: var(--card);
    box-shadow: 0 3px 10px rgba(0,0,0,.18);
    overflow: hidden;
  }
  .card-back { left: 580px; top: 80px; }
  .card-front { left: 60px; top: 560px; }

  .corner { position: absolute; left: 0; top: 0; }

  /* brand */
  .brand { display: flex; align-items: center; gap: 10px; }
  .brand-dot { width: 22px; height: 22px; border-radius: 50%; background: var(--green); }
  .brand-name { font-family: "Roboto Slab", Georgia, serif; font-weight: 300; color: var(--orange); font-size: 44px; line-height: 1; }
  .tagline { color: var(--green); font-weight: 700; font-size: 11px; letter-spacing: 2px; margin-top: 6px; }

  /* back */
  .card-back .brand { position: absolute; left: 150px; top: 80px; }
  .card-back .tagline { position: absolute; left: 184px; top: 132px; }
  .services { position: absolute; left: 0; right: 0; top: 160px; text-align: center; letter-spacing: 1.5px; }
  .services-lead { color: var(--orange); font-weight: 700; font-size: 14px; }
  .services-sub { color: var(--green); font-weight: 700; font-size: 13px; margin-top: 4px; }
  .apparatus { list-style: none; margin-top: 4px; color: var(--green); font-size: 13px; line-height: 16px; }
  .apparatus li::before { content: "\2022"; color: var(--orange); margin-right: 6px; }

  /* front */
  .card-front .logo-block { position: absolute; left: 36px; top: 200px; }
  .contact { position: absolute; left: 330px; top: 50px; }
  .person-name { color: var(--orange); font-weight: 700; font-size: 19px; letter-spacing: .5px; }
  .person-role { color: var(--ink); font-size: 13px; }
  .contact-lines { margin-top: 34px; font-size: 15px; line-height: 22px; color: var(--ink); }
  .contact-lines .label { color: var(--green); }
  .address { position: absolute; left: 330px; top: 222px; color: var(--ink); font-size: 15px; line-height: 19px; }
  .address-name { color: var(--orange); font-weight: 700; font-size: 17px; }
</style>
</head>
<body>

<section class="card card-back" aria-label="Card back">
  <svg class="corner" width="560" height="340" viewBox="0 0 560 340">
    <polygon points="0,0 260,0 0,70" fill="var(--green)"/>
    <polygon points="260,0 0,70 0,100" fill="var(--orange)"/>
  </svg>
  <div class="brand"><span class="brand-dot"></span><span class="brand-name">Motion Nest</span></div>
  <p class="tagline">BALANCE &nbsp; STRENGTH &nbsp; FLEXIBILITY</p>
  <div class="services">
    <p class="services-lead">SPECIALISING IN INDIVIDUAL PILATES INSTRUCTION</p>
    <p class="services-sub">MATWORK – including small apparatus and STUDIO:</p>
    <ul class="apparatus">
      <li>VIVANTE 3 GLIDER</li>
      <li>LADDER BARREL</li>
      <li>COUNTOUR BARREL</li>
      <li>FLEXI DOME</li>
      <li>VIM STOOL</li>
      <li>KIM-O-LAN</li>
    </ul>
  </div>
</section>

<section class="card card-front" aria-label="Card front">
  <svg class="corner" width="560" height="340" viewBox="0 0 560 340">
    <polygon points="0,0 200,0 0,95" fill="var(--green)"/>
    <polygon points="200,0 0,95 0,130" fill="var(--orange)"/>
  </svg>
  <div class="logo-block">
    <div class="brand"><span class="brand-dot"></span><span class="brand-name">Motion Nest</span></div>
    <p class="tagline">BALANCE &nbsp; STRENGTH &nbsp; FLEXIBILITY</p>
  </div>
  <div class="contact">
    <p class="person-name">MERIKA HOLLENBROOK</p>
    <p class="person-role">Dipl. of Professional Pilates Instruction</p>
    <p class="contact-lines">
      <span class="label">Mobile:</span> 041 555 0192<br>
      <span class="label">Email:</span> info@motionnest.com.au<br>
      <span class="label">Website:</span> www.motionnest.com.au
    </p>
  </div>
  <div class="address">
    <p class="address-name">MOTION NEST</p>
    <p>18 Larkspur Avenue, Wrenfield<br>WA 6031</p>
  </div>
</section>

</body>
</html>
```